Allergy Social Media Advertising Graphics Needed

We already have the copy written for ZV and Velmorix ads and need a designer to ad a graphic element to the campaign.

Target Market(s)

Mostly soccer moms, suburban Washington, DC, highly educated, smart and research oriented.

Font styles to use
Sans Serif

Requirements
Must have
• An eye-catching concept that makes people stop scrolling and pay attention to the advertisement.
Nice to have
• Clean and simple design. Bold approach with an elegant feel.
Should not have
• Too busy or cartoon-like designs.

```html
<!DOCTYPE html>
<html lang="en">
<head>
<meta charset="UTF-8">
<title>Peanut Allergy – Oral Immunotherapy</title>
<link rel="stylesheet" href="https://fonts.googleapis.com/css2?family=Montserrat:wght@300;400;500;600;700&display=swap">
<style>
  :root {
    --tan: #c2a76c;
    --brown: #7a5a28;
    --cream: #fff6d8;
    --navy-light: #33568f;
    --navy-dark: #263a62;
    --sky: #7cc6f7;
    --white: #ffffff;
    --ink: #111111;
  }
  * { margin: 0; padding: 0; box-sizing: border-box; }
  html, body { width: 1200px; height: 1200px; overflow: hidden; background: var(--white); }
  .ad {
    position: relative;
    width: 1200px;
    height: 1200px;
    overflow: hidden;
    background: var(--tan);
    font-family: "Montserrat", sans-serif;
  }
  .ad__shapes { position: absolute; inset: 0; }
  .headline { position: absolute; left: 0; top: 0; width: 1200px; }
  .headline__lead {
    position: absolute; left: 86px; top: 72px;
    font-size: 31px; font-weight: 500; color: var(--brown);
    white-space: nowrap;
  }
  .headline__lead span {
    font-size: 48px; font-weight: 400; color: var(--cream); margin-left: 6px;
  }
  .headline__main {
    position: absolute; left: 74px; top: 128px;
    font-size: 100px; line-height: 1; color: var(--cream);
    letter-spacing: -1px; white-space: nowrap;
  }
  .headline__main strong { font-weight: 700; }
  .headline__main em { font-style: normal; font-weight: 300; }
  .headline__tail {
    position: absolute; right: 106px; top: 244px;
    font-size: 36px; font-weight: 700; color: var(--brown);
    white-space: nowrap;
  }
  .body-copy {
    position: absolute; left: 69px; top: 398px; width: 1060px;
    color: var(--white); font-size: 28.5px; font-weight: 400; line-height: 37px;
  }
  .body-copy p { margin-bottom: 18px; }
  .body-copy .oit-line { font-size: 31px; margin-bottom: 14px; }
  .body-copy .oit-line strong { color: var(--sky); font-weight: 700; font-size: 45px; }
  .body-copy b { font-weight: 700; }
  .footer { position: absolute; left: 0; top: 983px; width: 1200px; height: 217px; background: var(--white); }
  .brand-mark {
    position: absolute; left: 69px; top: 33px; width: 144px; height: 144px;
    border: 3px solid var(--tan); border-radius: 50%;
    display: flex; align-items: center; justify-content: center;
    font-size: 26px; font-weight: 500; color: var(--ink);
  }
  .footer__cta {
    position: absolute; left: 330px; top: 44px; width: 540px; text-align: center;
    font-size: 31px; font-weight: 400; color: var(--brown);
  }
  .footer__url {
    position: absolute; left: 391px; top: 108px; width: 417px; height: 53px;
    border-radius: 27px; background: var(--tan);
    display: flex; align-items: center; justify-content: center;
    font-size: 31px; font-weight: 600; color: var(--white);
  }
</style>
</head>
<body>
<main class="ad">
  <svg class="ad__shapes" width="1200" height="1200" viewBox="0 0 1200 1200" aria-hidden="true">
    <defs>
      <linearGradient id="navy-fade" x1="0" y1="0" x2="1" y2="0">
        <stop offset="0" stop-color="#33568f"/>
        <stop offset="1" stop-color="#263a62"/>
      </linearGradient>
    </defs>
    <path d="M0 352 C 330 262, 760 240, 1200 440 L1200 1200 L0 1200 Z" fill="#ffffff"/>
    <path d="M0 354 C 330 276, 720 282, 1200 604 L1200 983 L0 983 Z" fill="url(#navy-fade)"/>
  </svg>

  <header class="headline">
    <p class="headline__lead">Is worrying about <span>Your Child’s</span></p>
    <h1 class="headline__main"><strong>Peanut</strong> <em>Allergy</em></h1>
    <p class="headline__tail">driving you nuts?</p>
  </header>

  <section class="body-copy">
    <p>Sleepovers. Play dates.<br>Restaurant outings. Normal activities<br>like these are potentially dangerous – even lethal –<br>for a child with a severe peanut allergy.</p>
    <p>Fortunately, there’s a treatment that can help reduce your child’s<br>risk of a serious allergic response.</p>
    <p class="oit-line">It’s called <strong>Oral Immunotherapy (OIT)</strong>,</p>
    <p><b>Halvern Allergy has been providing it since 2017</b>,<br>with excellent results.&nbsp; OIT is not a cure – it’s a desensitization<br>process that builds a child’s tolerance to an allergen over time.<br>We’re currently offering OIT for multiple food allergies, including<br>peanut, tree nuts, sesame, soy, milk, wheat and others.</p>
  </section>

  <footer class="footer">
    <div class="brand-mark">Halvern</div>
    <p class="footer__cta">Visit our website for details.</p>
    <p class="footer__url">www.website.com</p>
  </footer>
</main>
</body>
</html>
```